Brisk falcon athletics label

I am making labels for my supplement Brand I want some thing flashy and metallic as I’ll be using foil labels somthing with cannons and somthing intense like this tiger I have my logo alresdy so the logo super shiny silver
But bright neon colours else where good luck

Target Market(s)

Gym goers

Requirements
Nice to have
• I think instead of the tigers head a pirates head instead would be more fitting for my company

```html
<!DOCTYPE html>
<html lang="en">
<head>
<meta charset="utf-8">
<title>Brisk Falcon Athletics – Supplement Label</title>
<link rel="stylesheet" href="https://fonts.googleapis.com/css2?family=Oswald:wght@400;500;600;700&family=Arimo:wght@400;700;800&family=Michroma&display=swap">
<style>
  :root{
    --page:#ffffff;
    --forest-dark:#0b1713;
    --forest-mid:#1d3a33;
    --forest-light:#2c4d45;
    --gold:#f8c416;
    --ember:#f28a12;
    --fire:#c5400d;
    --silver:#e4e6e8;
    --white:#ffffff;
    --ink:#111111;
    --muted:#c9d3cf;
  }
  *{box-sizing:border-box;margin:0;padding:0}
  html,body{width:1200px;height:904px;overflow:hidden;background:var(--page)}
  body{position:relative;font-family:"Arimo",Arial,sans-serif}

  .label{
    position:absolute;left:20px;top:62px;width:1160px;height:780px;
    display:flex;overflow:hidden;
  }
  .label-backdrop{
    position:absolute;inset:0;
    background:
      radial-gradient(ellipse 40% 30% at 50% 62%, rgba(242,138,18,.28), transparent 70%),
      radial-gradient(ellipse 70% 60% at 50% 25%, var(--forest-light), transparent 75%),
      linear-gradient(180deg, var(--forest-mid) 0%, #14291f 60%, var(--forest-dark) 100%);
  }
  .panel{position:relative;height:100%}

  /* left panel */
  .panel-directions{width:250px;padding:64px 22px 0 26px;color:var(--white)}
  .directions-block{font-size:17px;line-height:1.23;color:#f1f1f1}
  .directions-rule{height:1px;background:rgba(255,255,255,.35);margin:22px 0}

  /* front panel */
  .panel-front{width:650px;text-align:center;color:var(--white)}
  .brand{position:absolute;top:78px;left:0;right:0;display:flex;justify-content:center;align-items:center;gap:12px}
  .brand-dot{width:14px;height:14px;border-radius:50%;background:var(--silver)}
  .brand-name{font-family:"Michroma",sans-serif;font-size:27px;letter-spacing:3px;color:var(--silver);text-transform:uppercase;line-height:1.3}
  .product-name{position:absolute;top:170px;left:0;right:0;font-family:"Oswald",sans-serif;font-weight:700;font-size:66px;line-height:1;color:var(--gold);letter-spacing:.5px}
  .flavour-name{position:absolute;top:262px;left:0;right:0;font-family:"Oswald",sans-serif;font-weight:600;font-size:36px;line-height:1;letter-spacing:.5px}
  .hero-art{
    position:absolute;left:40px;top:318px;width:570px;height:420px;border-radius:50% 50% 46% 46%/44% 44% 56% 56%;
    background:
      radial-gradient(ellipse 38% 30% at 50% 16%, rgba(197,64,13,.95), transparent 72%),
      radial-gradient(ellipse 50% 42% at 50% 62%, #ffd65a 0%, var(--ember) 45%, rgba(150,70,10,.6) 75%, transparent 100%);
  }
  .claims{position:absolute;top:598px;left:0;right:0;font-family:"Oswald",sans-serif;color:#2a1606}
  .claims-title{font-size:16px;font-weight:500}
  .claims-list{font-size:17px;font-weight:600;margin-top:10px;display:flex;justify-content:center;gap:6px}
  .claims-list span::before{content:"";display:inline-block;width:8px;height:8px;border-radius:50%;background:#2a1606;margin-right:3px;vertical-align:2px}
  .supplement-type{font-size:19px;font-weight:600;margin-top:20px}
  .net-weight{position:absolute;top:725px;left:0;right:0;font-family:"Oswald",sans-serif;font-weight:500;font-size:18px}

  /* right panel */
  .panel-info{width:260px;padding:34px 0 0 10px}
  .nutrition{background:var(--white);color:var(--ink);border:1px solid var(--ink);padding:3px 4px 4px;width:240px;font-size:9.5px;line-height:1.4}
  .nutrition h2{font-family:"Arimo",sans-serif;font-weight:800;font-size:24px;line-height:1;border-bottom:1px solid var(--ink);padding-bottom:2px}
  .nf-row{display:flex;justify-content:space-between;border-top:1px solid #888}
  .nf-thick{border-bottom:6px solid var(--ink)}
  .nf-mid{border-bottom:3px solid var(--ink)}
  .nf-cal{font-size:18px;font-weight:800;display:flex;justify-content:space-between}
  .nf-indent{padding-left:12px}
  .nf-indent2{padding-left:26px}
  .nf-note{font-size:7px;line-height:1.3;padding-top:3px;border-top:3px solid var(--ink)}
  .warning{margin-top:24px;color:var(--white);font-size:17px;line-height:1.2;padding-right:14px}
  .warning h3{color:var(--gold);font-size:19px;font-weight:700}
  .info-rule{height:2px;background:var(--white);margin:14px 14px 14px 0}
  .contact{color:var(--gold);font-weight:700;font-size:16px;line-height:1.4}
</style>
</head>
<body>
  <div class="label">
    <div class="label-backdrop" role="img" aria-label="Dark misty forest backdrop with glowing ember sparks"></div>

    <section class="panel panel-directions">
      <p class="directions-block">Lorem ipsum dolor sit amet, consectetuer adipiscing elit, sed diam nonummy nibh euismod tincidunt ut laoreet dolore magna aliquam erat volutpat. Ut wisi enim ad minim veniam, quis nostrud</p>
      <div class="directions-rule"></div>
      <p class="directions-block">Lorem ipsum dolor sit amet, sed diam nonummy nibh eui tincidunt ut laoreet dolore magna erat volutpat ad minim nostrud</p>
      <div class="directions-rule"></div>
      <p class="directions-block">Lorem ipsum dolor sit amet, sed diam nonummy nibh eui</p>
      <div class="directions-rule"></div>
      <p class="directions-block">These statements have not been evaluated by the Food and Drug Administration. Not intended to diagnose, treat, cure or prevent any disease.</p>
    </section>

    <section class="panel panel-front">
      <div class="brand">
        <span class="brand-dot"></span>
        <span class="brand-name">Brisk Falcon Athletics</span>
      </div>
      <h1 class="product-name">SUPPLEMENT NAME</h1>
      <p class="flavour-name">FLAVOUR NAME</p>
      <div class="hero-art" role="img" aria-label="Illustration of crossed firing cannons with a fiery explosion behind them"></div>
      <div class="claims">
        <p class="claims-title">SUPPORTS THE FOLLOWING:</p>
        <p class="claims-list"><span>MUSCLE GROWTH</span><span>STAMINA</span><span>ENDURANCE</span></p>
        <p class="supplement-type">DIETARY SUPPLEMENT</p>
      </div>
      <p class="net-weight">Net. Wt. 500GM</p>
    </section>

    <section class="panel panel-info">
      <div class="nutrition">
        <h2>Nutrition Facts</h2>
        <div>4 servings per container</div>
        <div class="nf-thick" style="display:flex;justify-content:space-between;font-weight:700"><span>Serving size</span><span>1 scoop</span></div>
        <div style="font-weight:700;font-size:8.5px">Amount Per Serving</div>
        <div class="nf-cal nf-mid"><span>Calories</span><span>140</span></div>
        <div style="text-align:right;font-weight:700;font-size:8px">% Daily Value*</div>
        <div class="nf-row"><span><b>Total Fat</b> 10g</span><b>13%</b></div>
        <div class="nf-row nf-indent"><span>Saturated Fat 1g</span><b>5%</b></div>
        <div class="nf-row nf-indent"><span><i>Trans</i> Fat 0g</span></div>
        <div class="nf-row"><span><b>Cholesterol</b> 0mg</span><b>0%</b></div>
        <div class="nf-row"><span><b>Sodium</b> 50mg</span><b>2%</b></div>
        <div class="nf-row"><span><b>Total Carbohydrate</b> 7g</span><b>3%</b></div>
        <div class="nf-row nf-indent"><span>Dietary Fiber 3g</span><b>11%</b></div>
        <div class="nf-row nf-indent"><span>Total Sugars 0g</span></div>
        <div class="nf-row nf-indent2"><span>Includes 0g Added Sugars</span><b>0%</b></div>
        <div class="nf-row nf-thick"><span><b>Protein</b> 2g</span></div>
        <div class="nf-row"><span>Vitamin D 0mcg</span><span>0%</span></div>
        <div class="nf-row"><span>Calcium 0mg</span><span>0%</span></div>
        <div class="nf-row"><span>Iron 1.26mg</span><span>6%</span></div>
        <div class="nf-row"><span>Potassium 0mg</span><span>0%</span></div>
        <p class="nf-note">*The % Daily Value (DV) tells you how much a nutrient in a serving of food contributes to a daily diet. 2,000 calories a day is used for general nutrition advice.</p>
      </div>
      <div class="warning">
        <h3>WARNING:</h3>
        <p>Keep out of reach of children. If you are pregnant, lactating or have a health condition, or are taking any medication, please consult a health professional before use.</p>
      </div>
      <div class="info-rule"></div>
      <address class="contact" style="font-style:normal">
        Brisk falcon athletics<br>
        Cedar Hollow,<br>
        BC, Canada<br>
        briskfalcon.example<br>
        +1 555-014-2287
      </address>
    </section>
  </div>
</body>
</html>
```